Business card design needed

I need a business card for a new company based in Perth, Western Australia, called KT Power Pty Ltd.

I'm the sole proprietor, and have 25 years' experience in directorship, senior commercial/business development/strategy roles in the oil & gas industry with both supermajors and junior listed companies. I also have interests in renewable energy (and am co-founder and director of a separate renewable energy start-up company). KT Power will be the vehicle for me to contract my services, principally in the oil & gas industry (although this will include directorship services to the renewable energy company). These services will include general consultancy in my areas of expertise, and contracting to provide senior management/director services to start-up or junior oil and gas companies.

I'm looking for a design that communicates professionalism, dynamism, experience, strategic skills and growth.

My ConnectHub profile may also be useful context;

"I have a real passion for discovering new investment opportunities and turning them from talk into reality. Right now my focus is on oil, gas and energy ventures. I’m always on the look out for compelling new investment opportunities where I can bring my leadership and strategic insight to bear to make a real difference by delivering transformational results.

I spent 24 years with HX where I built up extensive international experience in oil, gas and energy and was a member of the company’s “fast track” development programme. As an entrepreneurial senior commercial leader, strategic thinker and tactical dealmaker I was responsible for numerous deals such as divestments, farm-ins, asset swaps, new acreage bids, unitizations, gas and LNG sales, creating billions of dollars of value for HX. These deals frequently broke new ground and/or required an innovative approach that delivered results in excess of what the business thought achievable. I have held senior executive and director roles covering Exploration & Production, Mergers & Acquisitions, Business Development, LNG Marketing, Joint Venture Management, Gas & Power and Corporate head office. International assignments included UK, Australia, Indonesia, Norway & Belgium.

I’m a member of the Guild of Global Fuel Brokers (GGFB) and the Southern Council of Board Members (SCBM).

Board experience comprises four directorships and two alternate directorships of Australian companies, and directorship of a Not for Profit organisation.

Specialties
Strategy, Business Development, Mergers & Acquisitions, Joint Venture Management, Negotiation, Gas & LNG Marketing."

Target Market(s)

Oil and gas or energy companies of all sizes from large listed companies to start-ups - also service providers to the industry.

Industry/Entity Type

Oil And Gas

Contact Information for Business Card

KT Power Pty Ltd
Daniel Hobart
27C Lorne Avenue,
Kelmsdale,
WA 6093

Tel +61 455 823 617
email hobartdk@vellimo.net.au

```html
<!DOCTYPE html>
<html lang="en">
<head>
<meta charset="utf-8">
<title>KT Power Pty Ltd – Business Card</title>
<link rel="stylesheet" href="https://fonts.googleapis.com/css2?family=Fira+Sans:ital,wght@0,400;0,600;1,400;1,600&display=swap">
<style>
  :root {
    --ink: #2c3d60;
    --card: #f4f4f3;
    --backdrop: #d9d9d8;
    --edge: #c9c9c8;
  }
  * { margin: 0; padding: 0; box-sizing: border-box; }
  html, body {
    width: 1200px; height: 747px; overflow: hidden;
    background: var(--backdrop);
    font-family: "Fira Sans", sans-serif;
    color: var(--ink);
  }
  .canvas {
    position: relative; width: 1200px; height: 747px;
    display: flex; justify-content: center; align-items: center; gap: 90px;
  }
  .card {
    width: 366px; height: 600px;
    background: var(--card);
    box-shadow: 0 1px 0 var(--edge), 0 6px 18px rgba(0,0,0,0.12);
    position: relative;
    text-align: center;
  }
  /* front */
  .card-front .name {
    position: absolute; top: 64px; left: 0; right: 0;
    font-weight: 600; font-size: 23px; letter-spacing: 0.2px;
  }
  .divider { position: absolute; left: 78px; width: 210px; height: 10px; }
  .divider--top { top: 150px; }
  .divider--bottom { top: 345px; }
  .contact {
    position: absolute; top: 180px; left: 0; right: 0;
    font-size: 19px; line-height: 24px;
  }
  .contact .label { font-style: italic; font-weight: 600; }
  .company {
    position: absolute; top: 250px; left: 0; right: 0;
    font-size: 19px; line-height: 24px;
  }
  .company .company-name { font-weight: 600; font-style: italic; }
  .membership-intro {
    position: absolute; top: 392px; left: 0; right: 0;
    font-size: 15px;
  }
  .membership-council {
    position: absolute; top: 438px; left: 0; right: 0;
    font-size: 18px; line-height: 20px; text-transform: uppercase; letter-spacing: 0.5px;
  }
  .membership-guild {
    position: absolute; top: 512px; left: 0; right: 0;
    display: flex; justify-content: center; align-items: center; gap: 10px;
    font-size: 22px; font-weight: 600;
  }
  .membership-guild .mark {
    width: 44px; height: 44px; border-radius: 50%; background: var(--ink);
  }
  /* back */
  .brand {
    position: absolute; top: 92px; left: 0; right: 0;
    display: flex; flex-direction: column; align-items: center; gap: 10px;
  }
  .brand .mark {
    width: 16px; height: 16px; border-radius: 50%; background: var(--ink);
  }
  .brand .brand-name { font-size: 20px; font-weight: 600; }
  .specialties {
    position: absolute; top: 352px; left: 0; right: 0;
    list-style: none; font-size: 20px; line-height: 34px;
  }
  .specialties li::before, .specialties li::after { content: "•"; margin: 0 6px; }
</style>
</head>
<body>
<main class="canvas">
  <section class="card card-front">
    <h1 class="name">Daniel Hobart</h1>
    <svg class="divider divider--top" viewBox="0 0 210 10" aria-hidden="true">
      <line x1="0" y1="5" x2="210" y2="5" stroke="#2c3d60" stroke-width="1.4"/>
      <circle cx="105" cy="5" r="3.5" fill="#2c3d60"/>
    </svg>
    <p class="contact">
      <span class="label">t:</span> +61 455 823 617<br>
      <span class="label">e:</span> hobartdk@vellimo.net.au
    </p>
    <p class="company">
      <span class="company-name">KT Power Pty Ltd</span><br>
      27C Lorne Avenue<br>
      Kelmsdale, WA 6093
    </p>
    <svg class="divider divider--bottom" viewBox="0 0 210 10" aria-hidden="true">
      <line x1="0" y1="5" x2="210" y2="5" stroke="#2c3d60" stroke-width="1.4"/>
      <circle cx="105" cy="5" r="3.5" fill="#2c3d60"/>
    </svg>
    <p class="membership-intro">memeber of</p>
    <p class="membership-council">Southern Council<br>of Board Members</p>
    <p class="membership-guild"><span class="mark" aria-hidden="true"></span>GGFB</p>
  </section>

  <section class="card card-back">
    <div class="brand">
      <span class="mark" aria-hidden="true"></span>
      <span class="brand-name">KT Power</span>
    </div>
    <ul class="specialties">
      <li>Strategy</li>
      <li>Business Development</li>
      <li>Mergers &amp; Acquisitions</li>
      <li>Joint Venture Management</li>
      <li>Negotiation</li>
      <li>Gas &amp; LNG Marketing</li>
    </ul>
  </section>
</main>
</body>
</html>
```